250g Condiment Label

Hi, we are looking at re-vamping our 250g label. This is our main label, which covers 70% of our stock. It is overprinted on a thermal printer, it is used for jam, chutney, relish, marmalades etc. We would like to keep it similar so it's recognisable but feel like it could be better.
We require more space to fit the ingredients and a space to print the Best Before date. We do print a barcode on the label so require a space where artwork will not interfere with scanning.
Can the label be reduced to 208mm as it currently overlaps. The width of the band that wraps around the label is currently 4cm. This could go to a maximum of 5 cm. Our preference is to be approx 4.5cm. We would like to keep the security seal tab.
I've attached our current artwork. I'm hoping to see a few options based on this artwork.
Option 1. Please add an additional burgandy band around the base of the label (instead of the black line)
Option 2. More shadowing of the burgundy.
Option 3. Replace stripe background with logo background (as per 300g label sample attached)
Option 4: Your creative input
I would also like to see samples based of our 300g label, see attached. The dimensions need to be the same as the 250g label but lets see what it looks like in black.
1. Handmade Homestyle Quality around border
2. Dots around border
3. Your creative idea.
Please check our website for other labels in our range.
Sauce
Dressings
300g Gourmet https://larderbloom.com.au/gourmet-range/
250g https://larderbloom.com.au/jams/
Mustard & Aioli https://larderbloom.com.au/mustard-aioli-tapenades/
Sauce https://larderbloom.com.au/barbeque-sauce/
Dressings https://larderbloom.com.au/dressings-vinegars/

```html
<!DOCTYPE html>
<html lang="en">
<head>
<meta charset="utf-8">
<title>250g Condiment Label – Wrap Band Dieline</title>
<link href="https://fonts.googleapis.com/css2?family=Open+Sans:wght@400;700&family=Roboto:wght@400&display=swap" rel="stylesheet">
<style>
  :root{
    --black:#000;
    --gold:#9c7c3c;
    --gold-light:#d6b877;
    --cream:#fdf0c4;
    --cream-deep:#fbe7c4;
    --spec-blue:#2f6fb0;
    --safe-cyan:#2aa7df;
    --paper:#fff;
  }
  html,body{margin:0;padding:0;overflow:hidden;background:var(--paper);}
  .artboard{width:1200px;height:751px;position:relative;box-sizing:border-box;border:1px solid #e4e4e4;background:var(--paper);}
  .artboard svg{display:block;}
  .label-copy{font-family:"Open Sans",sans-serif;fill:#3a2e1a;}
  .spec-text{font-family:"Roboto",sans-serif;fill:var(--spec-blue);}
  .swatch-name{font-family:"Roboto",sans-serif;font-size:12px;fill:#111;}
  .swatch-cover{font-family:"Roboto",sans-serif;font-size:6px;fill:#111;}
</style>
</head>
<body>
<div class="artboard">
<svg width="1200" height="751" viewBox="0 0 1200 751" xmlns="http://www.w3.org/2000/svg">
  <defs>
    <pattern id="dot-row" width="11.45" height="10" patternUnits="userSpaceOnUse">
      <circle cx="5.7" cy="5" r="2.1" fill="var(--gold-light)"/>
    </pattern>
    <pattern id="dot-col" width="10" height="11.45" patternUnits="userSpaceOnUse">
      <circle cx="5" cy="5.7" r="2.1" fill="var(--gold-light)"/>
    </pattern>
    <linearGradient id="cream-field" x1="0" y1="0" x2="0" y2="1">
      <stop offset="0" stop-color="#fdf2cc"/>
      <stop offset="1" stop-color="#fbeabb"/>
    </linearGradient>
    <radialGradient id="emblem-tone" cx="0.5" cy="0.45" r="0.6">
      <stop offset="0" stop-color="#f3dfa8"/>
      <stop offset="0.6" stop-color="#c9a45e"/>
      <stop offset="1" stop-color="#7d5f2a"/>
    </radialGradient>
  </defs>

  <!-- wrap band -->
  <g class="wrap-band">
    <rect x="1026" y="437" width="95" height="209" fill="var(--cream-deep)"/>
    <rect x="140" y="437" width="886" height="209" fill="url(#cream-field)"/>
    <rect x="140" y="437" width="886" height="21" fill="var(--gold)"/>
    <rect x="140" y="458" width="886" height="26" fill="var(--black)"/>
    <rect x="140" y="609" width="886" height="4" fill="var(--gold)"/>
    <rect x="140" y="613" width="886" height="33" fill="var(--black)"/>
    <rect x="142" y="466" width="338" height="10" fill="url(#dot-row)"/>
    <rect x="603" y="466" width="421" height="10" fill="url(#dot-row)"/>
    <rect x="142" y="619" width="286" height="10" fill="url(#dot-row)"/>
    <rect x="672" y="619" width="352" height="10" fill="url(#dot-row)"/>
    <text x="548" y="627" text-anchor="middle" font-family="Open Sans,sans-serif" font-size="7.5" letter-spacing="4.2" fill="var(--gold-light)">HANDMADE HOMESTYLE QUALITY</text>
  </g>

  <!-- security seal tab -->
  <g class="seal-tab">
    <path d="M544 64 L624 144 L581 186 L581 397 L621 437 L467 437 L507 397 L507 186 L464 144 Z" fill="var(--gold)"/>
    <rect x="519" y="186" width="50" height="216" fill="var(--gold)"/>
    <line x1="523" y1="186" x2="523" y2="400" stroke="var(--black)" stroke-width="1"/>
    <line x1="565" y1="186" x2="565" y2="400" stroke="var(--black)" stroke-width="1"/>
    <rect x="529" y="186" width="30" height="216" fill="var(--black)"/>
    <rect x="539" y="194" width="10" height="194" fill="url(#dot-col)"/>
    <path d="M544 83 L603 144 L544 194 L484 144 Z" fill="var(--black)"/>
    <path d="M544 94 L593 144 L544 192 L496 144 Z" fill="url(#emblem-tone)" role="img" aria-label="Brand emblem illustration, gold tones"/>
  </g>

  <!-- front emblem and name plate -->
  <g class="front-emblem">
    <path d="M544 397 L618 459 L544 531 L469 459 Z" fill="var(--black)"/>
    <path d="M544 406 L600 462 L576 486 L512 486 L489 462 Z" fill="url(#emblem-tone)" role="img" aria-label="Brand emblem illustration, gold tones"/>
    <rect x="479" y="482" width="131" height="28" fill="var(--black)"/>
    <rect x="484" y="485" width="121" height="21" fill="var(--gold)"/>
    <text x="544.5" y="499.5" text-anchor="middle" font-family="Open Sans,sans-serif" font-weight="700" font-size="10" letter-spacing="1.5" fill="var(--black)">HOLLINS PRESERVES</text>
  </g>

  <!-- left panel copy -->
  <g class="label-copy maker-details" text-anchor="middle">
    <text x="223" y="502" font-size="9" font-weight="700">Proudly Australian</text>
    <text x="223" y="512" font-size="9" font-weight="700">owned and made</text>
    <text x="223" y="525" font-size="8.8">Larder Bloom Kitchen</text>
    <text x="223" y="534.5" font-size="8.8">14 Wattle Mill Road</text>
    <text x="223" y="544" font-size="8.8">Kanbella 2590</text>
    <text x="223" y="554" font-size="8.8">Ph (02) 4517 3390</text>
    <text x="223" y="563.5" font-size="8.8">www.larderbloom.com.au</text>
    <text x="223" y="578" font-size="9" font-weight="700">HACCP Accredited</text>
    <text x="223" y="590" font-size="7">Made on a production line that</text>
    <text x="223" y="598" font-size="7">also produces products containing</text>
    <text x="223" y="606" font-size="7">eggs, nuts, dairy and soy.</text>
  </g>

  <!-- nutrition panel -->
  <g class="label-copy nutrition-panel" font-size="8.5">
    <text x="817" y="497" font-weight="700">Nutritional Information</text>
    <text x="817" y="506" font-weight="700">Serving size</text>
    <text x="817" y="515" font-weight="700">Serves per pack</text>
    <line x1="814" y1="518" x2="966" y2="518" stroke="#3a2e1a" stroke-width="0.8"/>
    <text x="963" y="527" text-anchor="end">Per Serve  Per 100g</text>
    <line x1="814" y1="529.5" x2="966" y2="529.5" stroke="#3a2e1a" stroke-width="0.8"/>
    <text x="817" y="538">Energy</text>
    <text x="817" y="546.6">Protein</text>
    <text x="817" y="555.2">Fat, total</text>
    <text x="817" y="563.8">–Saturated</text>
    <text x="817" y="572.4">Carbohydrate</text>
    <text x="817" y="581">–Sugar</text>
    <text x="817" y="589.6">Sodium</text>
    <line x1="814" y1="593" x2="966" y2="593" stroke="#3a2e1a" stroke-width="0.8"/>
  </g>

  <!-- country of origin box -->
  <g class="origin-panel">
    <rect x="981" y="487" width="37" height="125" rx="3" fill="none" stroke="var(--black)" stroke-width="1.5"/>
    <g transform="translate(994 578) rotate(-90)" class="label-copy" font-size="7.2" font-weight="700">
      <text x="0" y="0">Made in Australia</text>
      <text x="0" y="8">from at least 63%</text>
      <text x="0" y="16">Australian ingredients</text>
    </g>
    <path d="M985 595 L1003 585 L1003 605 Z" fill="var(--black)"/>
    <rect x="1005" y="584" width="8" height="22" fill="none" stroke="var(--black)" stroke-width="1"/>
  </g>

  <!-- safe area guide -->
  <rect class="safe-area" x="153" y="450" width="956" height="184" fill="none" stroke="var(--safe-cyan)" stroke-width="0.6"/>
  <path d="M484 144 L544 83 L603 144 M573 187 L573 397 L618 440 M515 187 L515 397 L470 440" fill="none" stroke="var(--safe-cyan)" stroke-width="0.5"/>

  <!-- dimension annotations -->
  <g class="dimensions" stroke="var(--spec-blue)" stroke-width="0.6" fill="var(--spec-blue)">
    <line x1="370" y1="180" x2="489" y2="180"/>
    <line x1="370" y1="401" x2="489" y2="401"/>
    <line x1="381" y1="198" x2="381" y2="243"/>
    <line x1="381" y1="340" x2="381" y2="384"/>
    <path d="M381 181 L376 198 L386 198 Z" stroke="none"/>
    <path d="M381 400 L376 384 L386 384 Z" stroke="none"/>
    <line x1="78" y1="450" x2="140" y2="450"/>
    <line x1="78" y1="634" x2="140" y2="634"/>
    <line x1="90" y1="467" x2="90" y2="495"/>
    <line x1="90" y1="585" x2="90" y2="617"/>
    <path d="M90 451 L85 467 L95 467 Z" stroke="none"/>
    <path d="M90 633 L85 617 L95 617 Z" stroke="none"/>
    <line x1="153" y1="646" x2="153" y2="688"/>
    <line x1="1109" y1="646" x2="1109" y2="688"/>
    <line x1="170" y1="676" x2="580" y2="676"/>
    <line x1="683" y1="676" x2="1092" y2="676"/>
    <path d="M154 676 L170 671 L170 681 Z" stroke="none"/>
    <path d="M1108 676 L1092 671 L1092 681 Z" stroke="none"/>
  </g>
  <text class="spec-text" x="631" y="684" text-anchor="middle" font-size="20">208,00 мм</text>
  <text class="spec-text" transform="translate(373 292) rotate(90)" text-anchor="middle" font-size="20">45,00 MM</text>
  <text class="spec-text" transform="translate(98 541) rotate(-90)" text-anchor="middle" font-size="20">39,94 MM</text>

  <!-- ink swatches -->
  <g class="ink-swatches">
    <rect x="956" y="92" width="124" height="32" fill="#fff" stroke="#111" stroke-width="0.8"/>
    <rect x="956" y="92" width="22" height="23" fill="var(--black)"/>
    <line x1="956" y1="115" x2="1080" y2="115" stroke="#111" stroke-width="0.6"/>
    <text class="swatch-name" x="982" y="107">Black</text>
    <text class="swatch-cover" x="1018" y="121.5" text-anchor="middle">INK COVER: 10.89% - 26.29cm²</text>

    <rect x="956" y="136" width="124" height="32" fill="#fff" stroke="#111" stroke-width="0.8"/>
    <rect x="956" y="136" width="22" height="23" fill="#fdf0c4"/>
    <line x1="956" y1="159" x2="1080" y2="159" stroke="#111" stroke-width="0.6"/>
    <text class="swatch-name" x="982" y="151">C:0;M:4;Y:27;K:0</text>
    <text class="swatch-cover" x="1018" y="165.5" text-anchor="middle">INK COVER: 3.19% - 7.71cm²</text>

    <rect x="956" y="179" width="124" height="33" fill="#fff" stroke="#111" stroke-width="0.8"/>
    <rect x="956" y="179" width="22" height="24" fill="var(--gold)"/>
    <line x1="956" y1="203" x2="1080" y2="203" stroke="#111" stroke-width="0.6"/>
    <text class="swatch-name" x="982" y="195">PANTONE 8640 C</text>
    <text class="swatch-cover" x="1018" y="209.5" text-anchor="middle">INK COVER: 3.19% - 7.71cm²</text>

    <rect x="956" y="224" width="124" height="32" fill="#fff" stroke="#111" stroke-width="0.8"/>
    <rect x="956" y="224" width="22" height="23" fill="#fbe7c4"/>
    <line x1="956" y1="247" x2="1080" y2="247" stroke="#111" stroke-width="0.6"/>
    <text class="swatch-name" x="982" y="239">C:0;M:7;Y:25;K:1</text>
    <text class="swatch-cover" x="1018" y="253.5" text-anchor="middle">INK COVER: 3.19% - 7.71cm²</text>
  </g>
</svg>
</div>
</body>
</html>
```